Business Card Design

I have two logos , one is for the front of the card and the other for the back. The front image is the road and the sun, the back image should be the atom with the motto at the bottom. The back of the card should be black with the atom and lettering white. The front should have the image with the road and lettering black with the yellow sun all on a white background.
Updates

I have changed what I would like done. The only logo I want to use is the atom logo. White lettering with a black background on the front and back of the card. There should be no contact info on the back of the card. On the back there should b the logo with company name and the slogan underneath at the bottom of the card, also on the back if you can have the logo  image in the background as well in a gray or silver can be tiled or cascade of some sort.

On the front it should have all of the contact info with an email address added  tidewaveprints@fernmail.net   Black background with white lettering and another larger image of the logo in a gray or silver in the background. The logo and name side by side with the slogan directly under the name.

Industry/Entity Type

Business

Contact Information for Business Card

Colin Marsh
Director of Operations
6182 Hollis Ln #517
Georgetown, TX 78415
Cell: (512)487-3056
Fax: (512)871-4402

```html
<!DOCTYPE html>
<html lang="en">
<head>
<meta charset="utf-8">
<title>Pecan Valley Imaging – Business Cards</title>
<link rel="stylesheet" href="https://fonts.googleapis.com/css2?family=PT+Sans:wght@400;700&family=Questrial&display=swap">
<style>
  :root {
    --stage: #3a3a3a;
    --card-black: #050505;
    --accent-lime: #dde235;
    --silver: #2a2a2a;
    --silver-line: #3c3c3c;
    --icon: #dde235;
    --reverse-text: #ffffff;
    --soft-text: #d8d8d8;
  }
  * { box-sizing: border-box; margin: 0; padding: 0; }
  html, body { width: 1200px; height: 1000px; overflow: hidden; }
  body {
    background: var(--stage);
    display: flex;
    align-items: center;
    justify-content: center;
    gap: 60px;
  }
  .card {
    width: 520px;
    height: 300px;
    position: relative;
    overflow: hidden;
    background: var(--card-black);
    color: var(--reverse-text);
    box-shadow: 0 10px 30px rgba(0,0,0,.45);
  }
  .backdrop-circle {
    position: absolute;
    border-radius: 50%;
    background: var(--silver);
    border: 2px solid var(--silver-line);
  }

  /* Front (contact side) */
  .card--front { font-family: "PT Sans", sans-serif; }
  .card--front .backdrop-circle {
    width: 300px; height: 300px;
    right: -70px; top: 40px;
  }
  .accent-block {
    position: absolute;
    left: 0; top: 0;
    width: 128px; height: 118px;
    background: var(--accent-lime);
    border-bottom-right-radius: 22px;
  }
  .contact {
    position: absolute;
    left: 140px; top: 28px;
  }
  .contact__name {
    font-size: 17px;
    font-weight: 700;
    letter-spacing: .3px;
  }
  .contact__role {
    font-weight: 400;
    color: var(--soft-text);
  }
  .contact__list { list-style: none; margin-top: 8px; }
  .contact__item {
    display: flex;
    align-items: center;
    gap: 8px;
    font-size: 15px;
    line-height: 26px;
    color: var(--soft-text);
  }
  .contact__icon { width: 15px; height: 15px; flex: none; }
  .front-brand {
    position: absolute;
    right: 30px; bottom: 40px;
    display: flex;
    align-items: center;
    gap: 10px;
    font-size: 22px;
  }
  .front-brand__dot {
    width: 18px; height: 18px;
    border-radius: 50%;
    background: var(--accent-lime);
  }

  /* Back (brand side) */
  .card--back { font-family: "Questrial", sans-serif; }
  .card--back .backdrop-circle { width: 140px; height: 140px; }
  .card--back .backdrop-circle--a { left: -40px; top: -40px; }
  .card--back .backdrop-circle--b { left: 190px; top: 110px; }
  .card--back .backdrop-circle--c { right: -40px; top: -30px; }
  .back-brand {
    position: absolute;
    left: 150px; top: 70px;
    display: flex;
    align-items: center;
    gap: 14px;
    font-size: 24px;
  }
  .back-brand__dot {
    width: 16px; height: 16px;
    border-radius: 50%;
    background: var(--reverse-text);
  }
  .motto {
    position: absolute;
    left: 40px; right: 40px; bottom: 60px;
    display: flex;
    justify-content: space-between;
    list-style: none;
    font-size: 20px;
  }
</style>
</head>
<body>

  <section class="card card--front" aria-label="Business card, contact side">
    <div class="backdrop-circle" role="img" aria-label="Large silver company mark in the background"></div>
    <div class="accent-block"></div>

    <div class="contact">
      <p class="contact__name">COLIN MARSH <span class="contact__role">, Director of Operations</span></p>
      <ul class="contact__list">
        <li class="contact__item">
          <svg class="contact__icon" viewBox="0 0 16 16"><rect width="16" height="16" rx="2" fill="var(--icon)"/><rect x="5" y="3" width="6" height="10" rx="1" fill="#050505"/></svg>
          (512)487-3056
        </li>
        <li class="contact__item">
          <svg class="contact__icon" viewBox="0 0 16 16"><rect width="16" height="16" rx="2" fill="var(--icon)"/><rect x="3" y="6" width="10" height="6" fill="#050505"/><rect x="5" y="3" width="6" height="3" fill="#050505"/></svg>
          (512)871-4402
        </li>
        <li class="contact__item">
          <svg class="contact__icon" viewBox="0 0 16 16"><rect width="16" height="16" rx="2" fill="var(--icon)"/><rect x="3" y="4.5" width="10" height="7" fill="#050505"/><path d="M3 4.5 L8 8.5 L13 4.5" stroke="var(--icon)" stroke-width="1.2" fill="none"/></svg>
          tidewaveprints@fernmail.net
        </li>
        <li class="contact__item">
          <svg class="contact__icon" viewBox="0 0 16 16"><rect width="16" height="16" rx="2" fill="var(--icon)"/><path d="M3 8 L8 3.5 L13 8 V13 H3 Z" fill="#050505"/></svg>
          6182 Hollis Ln #517 Georgetown, TX 78415
        </li>
      </ul>
    </div>

    <div class="front-brand">
      <span class="front-brand__dot"></span>
      <span class="front-brand__name">Pecan Valley Imaging</span>
    </div>
  </section>

  <section class="card card--back" aria-label="Business card, brand side">
    <div class="backdrop-circle backdrop-circle--a" role="img" aria-label="Tiled silver company mark in the background"></div>
    <div class="backdrop-circle backdrop-circle--b" role="img" aria-label="Tiled silver company mark in the background"></div>
    <div class="backdrop-circle backdrop-circle--c" role="img" aria-label="Tiled silver company mark in the background"></div>
    <div class="back-brand">
      <span class="back-brand__dot"></span>
      <span class="back-brand__name">Pecan Valley Imaging</span>
    </div>
    <ul class="motto">
      <li>Professional</li>
      <li>Timely</li>
      <li>Accurate</li>
    </ul>
  </section>

</body>
</html>
```